Website Redesign Project

Bright Harbour Consulting provides project management and project controls consultancy services to companies in many industry sectors, within Australia and overseas. My company has been developing a business brand through forging strong business relationships within industry. We provide innovative tools, concepts and solutions to management teams to assist them in better plan and managing there project portfolios.
SECTORS OF INDUSTRY WE SERVICE
★Oil & Gas
★Minerals & Metals
★Petrochemical
★Manufacturing
★Building & Construction
★Telecommunications
★Rail
★Civil
OLD WEBSITE
My old website www.brightharbourconsulting.com.au needs a complete overhaul in terms of how the web pages look and feel. I am trying to get away from the grey, washed out look as it is uninviting and dull. My clients commented that my webpage does not reflect who I am as a company or my core values. Think total redesign
DESIGN
I would like a webpage design that is modern and has a corporate image. It must be elegant, classy, and have an overall glossy appearance. I want something exciting that creates some excellent feedback from clients. It needs to have a savvy appearance and an attitude of a market leader. A generic website template cannot be used as I provide a unique service to clients. I do not need a website design that looks like my compeditors, I want something that stands out in the crowd and effectivly markets my bussinesses brand. I want my website to represent quality, so only high resolution images that are clear, sharp and in focus can be used. With this design, throw your standard webpage design concepts out the window, as I want something fresh, innovative, exciting and inviting. The overall design should appear uncluttered as all content needs to be there for a reason, so think functional.
It must be professional and of the highest calibre as my clients expect nothing less. I provide clients with innovative tools, concepts and solutions, so the design needs to be edgy and creative to align with my company’s core business services. The new design must promote the company’s brand and us as a market leader. It must communicate that we service many industry sectors and reflect our company’s creativity, vision, energy and drive.
WEBPAGE WRITTEN CONTENT
I am happy with the written content on each page within my old website. You may arrange the text how you see fit within the new design. On the main page of my old website the text is under scored, I am not a big fan of this. I currently do not like the format the text is in, I am looking for a formatt that is easy to read, looks flattering and pleasing to the eye.
MAIN PAGE DESIGN
The main page design needs to focus on my company as a brand, it must promote that I service many industry sectors. My old webpage had me pigeon holed as only providing services to oil and gas. This is incorrect as I service oil & gas, metals and minerals, Petrochemical, Manufacturing, Building & Construction, Telecommunications, Rail and civil.
WEBPAGE COLUR PREFERENCE
Prefer a white background with plenty of colour
TESTIMONIAL TAB
The testimonial tab on the task bar can be removed as it is no longer required.
FINISHED PRODUCT
The finished product will be uploaded by you to a nominated web hosting account. I will need a copy of all files associated with the design. A copy of the finished product will also be provided in formats that can me imported to Xara Pro Designer as I will update my website in 6 months or so using this tool.
Updates
I have updated the design brief after recieving feedback from several designers
Thanks
Hi All
I have just launched another project called "bright harbour consulting business card redesign project", you are all welcome to join this project.
Thanks
Target Market(s)
★Oil and Gas
★Mining and Resources
★Building and infrastructure
★Petrochemical
★Civil and roads
★Rail
Industry/Entity Type
Industry
Requirements
Must have
- ★Draw you in
★Hold your attention
★Identify company brand
★Highlight skills experience and expertise
★Be a unique design not generic
Should not have
- ★The webpage design should not be old fashioned
★ The design should not be based off a generic design template
★The webpage should not be cluttered; everything needs to be there for a reason.

```html
<!DOCTYPE html>
<html lang="en">
<head>
<meta charset="utf-8">
<title>Bright Harbour Consulting</title>
<link href="https://fonts.googleapis.com/css2?family=Arimo:wght@400;700&display=swap" rel="stylesheet">
<style>
:root{
  --sky-top:#1f5fae;
  --sky-bottom:#4a9ad6;
  --nav:#1aa6da;
  --nav-light:#3cc3ec;
  --nav-dark:#0d7fb0;
  --red:#ee2a32;
  --white:#ffffff;
  --ink:#222222;
  --muted:#666666;
  --link:#1a8ec4;
  --footer-text:#e8f2fb;
}
*{margin:0;padding:0;box-sizing:border-box}
html,body{width:987px;height:1200px;overflow:hidden}
body{position:relative;font-family:"Arimo",Arial,sans-serif;background:linear-gradient(180deg,var(--sky-top) 0%,#2d7cc4 45%,var(--sky-bottom) 100%);color:var(--ink)}
.abs{position:absolute}
.contact-email{right:155px;top:7px;font-size:10px;color:var(--white)}
.contact-phone{right:154px;top:22px;font-size:20px;color:var(--white);display:flex;align-items:center;gap:8px}
.contact-phone .dot{width:15px;height:15px;border-radius:50%;background:var(--nav-light);display:inline-block}
.panel{left:115px;top:56px;width:760px;height:994px;background:var(--white)}
.brand{left:170px;top:82px}
.brand-name{font-size:18px;font-weight:700;color:var(--red);display:flex;align-items:center;gap:8px;letter-spacing:-.2px}
.brand-name .mark{width:20px;height:20px;background:var(--ink);display:inline-block}
.brand-tag{font-size:6.5px;color:var(--ink);margin-top:4px;margin-left:28px}
.nav-fold{top:183px;width:0;height:0;border-top:23px solid var(--nav-dark)}
.nav-fold.left{left:99px;border-left:16px solid transparent}
.nav-fold.right{left:875px;border-right:16px solid transparent}
.nav{left:99px;top:139px;width:792px;height:44px;background:linear-gradient(180deg,var(--nav-light),var(--nav));display:flex;align-items:center;padding-left:60px}
.nav a{font-size:10px;color:var(--white);text-decoration:none;height:29px;line-height:29px;padding:0 17px;border-right:1px solid rgba(255,255,255,.25)}
.nav a:last-child{border-right:none}
.nav a.active{background:var(--red);padding:0 21px}
.hero{left:155px;top:214px;width:679px;height:323px;background:linear-gradient(180deg,#2e6cc9 0%,#5f94dc 18%,#c6d7ec 34%,#aeb8c0 46%,#d4d8da 56%,#8e979d 68%,#3f74a6 80%,#5b8cba 86%,#c9cdd0 100%)}
.hero-arrow{top:352px;font-size:44px;color:#1d1d1d;font-weight:400}
.hero-dots{left:738px;top:229px;display:flex;gap:6px}
.hero-dots i{width:8px;height:8px;border-radius:50%;background:#ddd;display:block}
.hero-dots i.on{background:var(--red)}
.bar{background:var(--red);color:var(--white);font-size:13px;display:flex;align-items:center;padding-left:9px}
.news-bar{left:152px;top:568px;width:215px;height:35px}
.comments-bar{left:152px;top:754px;width:215px;height:35px;padding-left:11px}
.sectors-bar{left:403px;top:755px;width:430px;height:33px;padding-left:11px}
.news{left:160px;top:611px;width:195px}
.news-item{padding-bottom:10px;margin-bottom:10px;border-bottom:1px dotted #555}
.news-date{font-size:10.5px;color:var(--ink)}
.news-date::before{content:"\2192";margin-right:5px}
.news-text{font-size:8.4px;font-style:italic;color:var(--muted);margin-left:14px;width:165px;line-height:1.05}
.more{font-size:8px;color:var(--red);text-align:right}
.welcome{left:406px;top:586px;width:398px}
.welcome h1{font-size:11.5px;font-weight:400;color:var(--ink)}
.welcome h1 span{font-size:17px;color:var(--red)}
.welcome p{font-size:9.2px;line-height:1.08;color:var(--ink);margin-top:10px}
.welcome p:first-of-type{margin-top:18px}
.welcome .more{margin-top:9px;margin-right:-14px}
.comments{left:159px;top:807px;width:196px}
.comment{font-size:8.4px;color:var(--muted);line-height:1.05;padding-bottom:11px;margin-bottom:14px;border-bottom:1px dotted #555}
.sector{width:98px;text-align:center}
.sector .thumb{width:98px;height:71px}
.sector span{display:block;margin-top:9px;font-size:8.6px;color:var(--link);text-decoration:underline}
.footer-h{font-size:13px;color:var(--white);padding-bottom:4px;border-bottom:1px dotted rgba(255,255,255,.5)}
.flinks{font-size:9.2px;color:var(--footer-text);line-height:17px}
.fcol-rule{border-right:1px dotted rgba(255,255,255,.35);height:66px}
.social{left:775px;top:1091px;display:flex;flex-direction:column;gap:6px}
.social i{width:16px;height:16px;display:block;background:var(--nav-light)}
.social i.warm{background:#f07a22}
.copyright{left:152px;top:1183px;font-size:8.6px;color:var(--footer-text)}
</style>
</head>
<body>
<div class="abs contact-email">Email: contact@brightharbourconsulting.com.au</div>
<div class="abs contact-phone"><i class="dot"></i>+61 0400 555 018</div>

<div class="abs panel"></div>

<div class="abs brand">
  <div class="brand-name"><i class="mark"></i>BRIGHT HARBOUR CONSULTING</div>
  <div class="brand-tag">Providing Effective Project Controls and Management Solutions</div>
</div>

<div class="abs nav-fold left"></div>
<div class="abs nav-fold right"></div>
<nav class="abs nav">
  <a class="active">Home</a><a>About Us</a><a>Expertise</a><a>Knowledge</a><a>Experience</a><a>Projects</a><a>Focus</a><a>Recuitment</a><a>Contact</a>
</nav>

<div class="abs hero" role="img" aria-label="Offshore oil and gas processing platform with chimneys and pipework under a blue sky, open sea behind"></div>
<div class="abs hero-arrow" style="left:175px">&#8249;</div>
<div class="abs hero-arrow" style="left:784px">&#8250;</div>
<div class="abs hero-dots"><i class="on"></i><i></i><i></i></div>

<div class="abs bar news-bar">LATEST NEWS</div>
<div class="abs news">
  <div class="news-item"><div class="news-date">21/06/2013</div><div class="news-text">Sed nisi turpis, pellentesque at ultrices in, dapibus in magna.</div></div>
  <div class="news-item"><div class="news-date">21/06/2013</div><div class="news-text">Sed nisi turpis, pellentesque at ultrices in, dapibus in magna.</div></div>
  <div class="more" style="margin-top:-4px">read more..</div>
</div>

<section class="abs welcome">
  <h1>WELCOME TO <span>BRIGHT HARBOUR CONSULTING</span></h1>
  <p>&nbsp;I provide services to companies in the mining and oil and gas sector to enabling them to plan and manage their construction projects more effectively. This is achieved by evaluating the businesses practices and them implementing different tools and solutions.</p>
  <p>My clients are then able to plan and deliver their projects, on time and within their budgets. I am able to provide services to both large and small scale businesses within Australian and Over-seas. I offer my clients value by providing, exceptional skills and expertise at a competitive market rate.</p>
  <div class="more">read more</div>
</section>

<div class="abs bar comments-bar">RECENT COMMENTS</div>
<div class="abs comments">
  <div class="comment">Noel Hartigan commented on<br>Lorem ipsum dolor sit amet, consectetuer<br>October 04, 2012</div>
  <div class="comment">Greg Pellow commented on<br>Lorem ipsum dolor sit amet, consectetuer<br>October 04, 2012</div>
  <div class="comment">Sam Okafor commented on<br>Lorem ipsum dolor sit amet, consectetuer<br>October 04, 2012</div>
  <div class="comment">Sam Okafor commented on<br>Lorem ipsum dolor sit amet, consectetuer<br>October 04, 2012</div>
  <div class="more" style="margin-top:-4px">read more..</div>
</div>

<div class="abs bar sectors-bar">SECTORS OF INDUSTRY WE SERVICE</div>
<div class="abs sector" style="left:406px;top:804px"><div class="thumb" role="img" aria-label="Oil and gas processing plant" style="background:linear-gradient(180deg,#6fa3dc 0%,#b9d0e8 35%,#9aa3a8 60%,#e2e0da 100%)"></div><span>Oil and gas</span></div>
<div class="abs sector" style="left:512px;top:804px"><div class="thumb" role="img" aria-label="Polished metal sheets" style="background:linear-gradient(120deg,#5a72a8 0%,#e6ecf6 30%,#7f95c4 55%,#f0f2f8 75%,#5d74ad 100%)"></div><span>Minerals and Metals</span></div>
<div class="abs sector" style="left:617px;top:804px"><div class="thumb" role="img" aria-label="Petrochemical refinery" style="background:linear-gradient(180deg,#5f98d8 0%,#a9c6e6 40%,#8a8474 62%,#5d5a50 100%)"></div><span>Petrochemical</span></div>
<div class="abs sector" style="left:723px;top:804px"><div class="thumb" role="img" aria-label="Satellite dish antenna" style="background:linear-gradient(180deg,#2f78d0 0%,#6fa4e0 45%,#c9dbef 80%,#e4ecf6 100%)"></div><span>Telecommunication</span></div>
<div class="abs sector" style="left:406px;top:904px"><div class="thumb" role="img" aria-label="Robotic manufacturing line" style="background:linear-gradient(135deg,#cf7a2e 0%,#8f6a50 35%,#4f6a8f 65%,#9aa4b0 100%)"></div><span>Manufacturing</span></div>
<div class="abs sector" style="left:512px;top:904px"><div class="thumb" role="img" aria-label="Apartment building" style="background:linear-gradient(180deg,#4f90dc 0%,#a7c8ec 30%,#eceeee 50%,#d6d8da 80%,#8aa070 100%)"></div><span>Building &amp; Construction</span></div>
<div class="abs sector" style="left:617px;top:904px"><div class="thumb" role="img" aria-label="High speed train at a station" style="background:linear-gradient(135deg,#3a3e44 0%,#c8ced4 35%,#eef0f2 55%,#e0602a 70%,#6b7480 100%)"></div><span>Rail</span></div>
<div class="abs sector" style="left:723px;top:904px"><div class="thumb" role="img" aria-label="Curved steel bridge over water" style="background:linear-gradient(180deg,#5f96d8 0%,#c3d6ea 45%,#9aa6ae 65%,#5f7a58 100%)"></div><span>Civil</span></div>

<div class="abs footer-h" style="left:152px;top:1058px;width:242px">QUICK LINKS</div>
<div class="abs flinks" style="left:152px;top:1083px">Home<br>About Us<br>Expertise<br>Knowledge</div>
<div class="abs fcol-rule" style="left:220px;top:1086px"></div>
<div class="abs flinks" style="left:245px;top:1083px">Projects<br>Focus<br>Recuitment<br>Contact</div>
<div class="abs fcol-rule" style="left:303px;top:1086px"></div>
<div class="abs flinks" style="left:334px;top:1084px">Experience<br>Services<br>Blog</div>

<div class="abs footer-h" style="left:468px;top:1058px;width:234px">SERVICES</div>
<div class="abs flinks" style="left:468px;top:1083px">Oil and gas<br>Minerals and metals<br>Petrochemical<br>Manufacturing</div>
<div class="abs fcol-rule" style="left:563px;top:1086px"></div>
<div class="abs flinks" style="left:593px;top:1084px">Building and Construction<br>Telecommunication<br>Civil<br>Rail</div>

<div class="abs footer-h" style="left:756px;top:1058px;width:73px">Follows Us</div>
<div class="abs social"><i></i><i></i><i></i><i class="warm"></i></div>

<div class="abs copyright">Copyright &copy; 2013 Bright Harbour Consulting.&nbsp; All rights reserved...</div>
</body>
</html>
```